Card design for Heating and Cooling company

this is for a heating and cooling company we recently updated our logo and need to update our cards. We attached our logo so you can incorporate it into the card. We specialize in residential and commercial furnace and air condition repairs. Have been in business since 2014.

Phone number 555.284.9137

We need the following phrases
:Repairs, Installations, and maintenance
:Quality work at reasonable prices
:residential/commercial
:Licensed &Insured
:Email Pinegrovehvac47@mailbox-example.com
Name: Teodor K (Ted)
Also on back side I would like my logo with wording :Thank you for your business and refferal

Industry/Entity Type

Hvac

Contact Information for Business Card

:residential/commercial
:Licensed & Insured
Name: Teodor K (Ted)
Number:555.284.9136

Requirements
Must have
• Blue and red colors
Nice to have
• Maybe a pic of a furnace or air conditioner

```html
<!DOCTYPE html>
<html lang="en">
<head>
<meta charset="utf-8">
<title>Pinegrove Heating &amp; Cooling – Business Card</title>
<link href="https://fonts.googleapis.com/css2?family=Lato:wght@400;500;700;900&display=swap" rel="stylesheet">
<style>
  :root {
    --backdrop: #8c8c8c;
    --card: #ffffff;
    --ink: #1f1f1f;
    --brand-blue: #1ea3ea;
    --brand-red: #f0201c;
    --rule: #222222;
    --photo-light: #e9eaec;
    --photo-mid: #c9ccd0;
  }
  * { margin: 0; padding: 0; box-sizing: border-box; }
  html, body { width: 1200px; height: 1200px; overflow: hidden; }
  body {
    background: var(--backdrop);
    font-family: "Lato", sans-serif;
    color: var(--ink);
    position: relative;
  }
  .card {
    position: absolute;
    top: 310px;
    height: 594px;
    background: var(--card);
    box-shadow: 2px 3px 6px rgba(0,0,0,0.35);
  }
  .card--front { left: 234px; width: 364px; }
  .card--back { left: 627px; width: 369px; }

  .brand {
    position: absolute;
    left: 0; right: 0;
    top: 118px;
    display: flex;
    flex-direction: column;
    align-items: center;
    gap: 14px;
  }
  .brand__dot {
    width: 46px; height: 46px;
    border-radius: 50%;
    background: var(--brand-blue);
  }
  .brand__name {
    font-weight: 900;
    font-size: 40px;
    letter-spacing: 1px;
    color: var(--brand-blue);
    line-height: 1;
  }

  .holder {
    position: absolute;
    left: 0; right: 0;
    top: 343px;
    text-align: center;
    font-size: 21px;
    font-weight: 500;
    line-height: 1.2;
  }
  .holder__name { color: var(--brand-blue); }
  .holder__nick { color: var(--brand-red); }

  .rule {
    position: absolute;
    left: 82px;
    width: 201px;
    height: 1px;
    background: var(--rule);
  }
  .rule--top { top: 380px; }
  .rule--bottom { top: 453px; }

  .contact {
    position: absolute;
    left: 0; right: 0;
    top: 394px;
    text-align: center;
    font-size: 17px;
    line-height: 22px;
  }
  .contact__email { font-size: 15.5px; }

  .services {
    position: absolute;
    left: 0; right: 0;
    top: 468px;
    text-align: center;
    font-size: 16.5px;
    line-height: 21.5px;
  }

  .equipment-photo {
    position: absolute;
    left: 7px;
    top: 105px;
    width: 341px;
    height: 320px;
    background: linear-gradient(160deg, var(--photo-light) 0%, var(--photo-mid) 100%);
  }

  .thanks {
    position: absolute;
    left: 0; right: 0;
    top: 486px;
    text-align: center;
    font-size: 27px;
    font-weight: 500;
    line-height: 32px;
    text-transform: uppercase;
    color: var(--ink);
  }
</style>
</head>
<body>
  <section class="card card--front">
    <div class="brand">
      <div class="brand__dot"></div>
      <div class="brand__name">PINEGROVE</div>
    </div>
    <p class="holder"><span class="holder__name">TEODOR K</span> <span class="holder__nick">(TED)</span></p>
    <div class="rule rule--top"></div>
    <div class="contact">
      <p class="contact__phone">555.284.9136</p>
      <p class="contact__email">Pinegrovehvac47@mailbox-example.com</p>
    </div>
    <div class="rule rule--bottom"></div>
    <div class="services">
      <p>Repairs, Installations, and maintenance</p>
      <p>Residential/commercial</p>
      <p>Quality work at reasonable prices</p>
      <p>Licensed &amp; Insured</p>
    </div>
  </section>

  <section class="card card--back">
    <div class="equipment-photo" role="img" aria-label="Product photo of a wall-mounted air conditioner, remote control, outdoor condenser unit and a furnace"></div>
    <p class="thanks">Thank you for your<br>business and refferal</p>
  </section>
</body>
</html>
```